Corvane Tables business cards

I’d like a business card design that includes my logo, a tag line and my contact info. Black, textured background. My contact info color should match the orange and blue gradients. Tagline under logo: “Wooden Tables and Furniture of the Highest Quality”

Target Market(s)

High end furniture buyers

Contact Information for Business Card

Contact info, logo and tagline

```html
<!DOCTYPE html>
<html lang="en">
<head>
<meta charset="utf-8">
<title>Corvane Tables – Business Cards</title>
<link href="https://fonts.googleapis.com/css2?family=Tenor+Sans&display=swap" rel="stylesheet">
<style>
  :root {
    --page: #2b2b2e;
    --card-black: #050505;
    --card-grey: #4a4a4c;
    --tree-grey: #5e5e60;
    --orange: #f08a4b;
    --orange-soft: #f4a070;
    --blue: #4d9be0;
    --blue-soft: #7ab8ee;
    --font: "Tenor Sans", "Trebuchet MS", sans-serif;
  }
  * { box-sizing: border-box; margin: 0; padding: 0; }
  html, body { width: 1200px; height: 900px; overflow: hidden; }
  body { background: var(--page); font-family: var(--font); position: relative; }

  .card {
    position: absolute;
    left: 250px;
    width: 700px;
    height: 400px;
    border-radius: 34px;
    overflow: hidden;
    background: var(--card-black);
    box-shadow: 0 14px 30px rgba(0,0,0,.55);
  }
  .card--front { top: 35px; }
  .card--back { top: 465px; }

  /* Front */
  .front-tree-art {
    position: absolute; inset: 0;
    background:
      radial-gradient(ellipse 55% 70% at 55% 30%, rgba(70,70,72,.55), transparent 70%),
      linear-gradient(180deg, transparent 0 45%, rgba(74,74,76,.9) 62%, var(--card-grey) 100%);
  }
  .brand {
    position: absolute;
    display: flex; align-items: center; gap: 14px;
  }
  .brand-dot {
    width: 22px; height: 22px; border-radius: 50%;
    background: var(--orange);
  }
  .brand-name {
    font-size: 62px; color: var(--orange); line-height: 1; letter-spacing: .5px;
    white-space: nowrap;
  }
  .brand-llc {
    position: absolute; font-size: 14px; color: var(--orange); letter-spacing: 1px;
  }
  .front .brand { left: 130px; top: 150px; }
  .front .brand-llc { left: 596px; top: 214px; }
  .front .brand-rule {
    position: absolute; left: 380px; top: 222px; width: 210px; height: 1px; background: var(--orange);
  }
  .tagline {
    position: absolute; left: 166px; top: 240px;
    font-size: 25px; color: var(--blue); letter-spacing: .5px; white-space: nowrap;
  }
  .front-web {
    position: absolute; left: 0; right: 0; top: 330px;
    display: flex; align-items: center; gap: 16px;
  }
  .front-web-rule { width: 250px; height: 1.5px; background: var(--orange); }
  .front-web-text { font-size: 22px; color: var(--orange-soft); letter-spacing: 2.5px; white-space: nowrap; }

  /* Back */
  .back-field {
    position: absolute; inset: 0;
    background: linear-gradient(160deg, var(--card-grey) 0%, #444446 45%, #1a1a1a 62%, var(--card-black) 72%);
  }
  .back .brand { left: 70px; top: 60px; }
  .back .brand-rule {
    position: absolute; left: 300px; top: 132px; width: 260px; height: 1px; background: var(--orange);
  }
  .back .brand-llc { left: 566px; top: 124px; }
  .grove-art {
    position: absolute; left: 20px; bottom: 0; width: 330px; height: 190px;
    background: linear-gradient(180deg, rgba(110,110,112,.55) 0%, rgba(90,90,92,.45) 50%, rgba(30,30,30,.2) 100%);
    border-radius: 40% 40% 0 0 / 30% 30% 0 0;
  }
  .contact {
    position: absolute; left: 366px; top: 190px; right: 24px;
    list-style: none; color: var(--orange-soft); font-size: 20px; letter-spacing: .8px;
  }
  .contact li { display: flex; align-items: flex-start; gap: 12px; margin-bottom: 10px; line-height: 1.25; white-space: nowrap; }
  .contact-icon {
    flex: none; width: 24px; height: 24px; border-radius: 4px;
    background: var(--blue); display: flex; align-items: center; justify-content: center; margin-top: 1px;
  }
  .contact-icon svg { width: 16px; height: 16px; }
</style>
</head>
<body>

<section class="card card--front front" aria-label="Card front">
  <div class="front-tree-art" role="img" aria-label="Large faint tree silhouette spreading across the card"></div>
  <div class="brand">
    <span class="brand-dot"></span>
    <span class="brand-name">Corvane Tables</span>
  </div>
  <span class="brand-rule"></span>
  <span class="brand-llc">LLC</span>
  <p class="tagline">High quality, handcrafted furniture</p>
  <div class="front-web">
    <span class="front-web-rule"></span>
    <span class="front-web-text">www.corvanetables.com</span>
  </div>
</section>

<section class="card card--back back" aria-label="Card back">
  <div class="back-field"></div>
  <div class="brand">
    <span class="brand-dot"></span>
    <span class="brand-name">Corvane Tables</span>
  </div>
  <span class="brand-rule"></span>
  <span class="brand-llc">LLC</span>
  <div class="grove-art" role="img" aria-label="Row of bare grey trees along the bottom edge"></div>
  <ul class="contact">
    <li>
      <span class="contact-icon"><svg viewBox="0 0 16 16"><path d="M8 1a5 5 0 0 0-5 5c0 4 5 9 5 9s5-5 5-9a5 5 0 0 0-5-5z" fill="#fff"/><circle cx="8" cy="6" r="2" fill="#4d9be0"/></svg></span>
      <span>Address Line<br>City, State, Postcode</span>
    </li>
    <li>
      <span class="contact-icon"><svg viewBox="0 0 16 16"><path d="M4 1.5l2.5 3-1.5 1.6a8 8 0 0 0 4.9 4.9l1.6-1.5 3 2.5-1.5 2.5C7 14.5 1.5 9 1.5 3z" fill="#fff"/></svg></span>
      <span>555 - 555555</span>
    </li>
    <li>
      <span class="contact-icon"><svg viewBox="0 0 16 16"><rect x="1.5" y="3.5" width="13" height="9" fill="none" stroke="#fff" stroke-width="1.4"/><path d="M1.5 3.5l6.5 5 6.5-5" fill="none" stroke="#fff" stroke-width="1.4"/></svg></span>
      <span>info@corvanetables.com</span>
    </li>
    <li>
      <span class="contact-icon"><svg viewBox="0 0 16 16"><path d="M3 1.5v12l3-3 2 4.5 2-1-2-4.3h4.5z" fill="#fff"/></svg></span>
      <span>www.corvanetables.com</span>
    </li>
  </ul>
</section>

</body>
</html>
```